Eye catching business card

2 sided
Black background with logo in color on one side along with the words "Proudly serving the commercial and defense industries since 1975"
2nd side to contain contact information (see attached current business card) and "Waterjet, Composite, Precision Machining and Clean Room Manufacturing" with a very faint watermark of a waving USA Flag in the back ground.
Remove the "est. 195" from the current logo design

```html
<!DOCTYPE html>
<html lang="en">
<head>
<meta charset="utf-8">
<title>Meridian Fabrication Inc — Business Card</title>
<link href="https://fonts.googleapis.com/css2?family=Montserrat:wght@400;500;600&display=swap" rel="stylesheet">
<style>
  :root {
    --stage: #4b4b4c;
    --card: #1c1c1c;
    --blue: #3a8fd9;
    --grey: #b0b0b0;
    --grey-soft: #9a9a9a;
    --flag-red: #b8323a;
    --flag-blue: #3c5fa8;
  }
  * { margin: 0; padding: 0; box-sizing: border-box; }
  html, body { width: 875px; height: 1200px; overflow: hidden; }
  body {
    background: var(--stage);
    font-family: "Montserrat", sans-serif;
    position: relative;
  }
  .card {
    position: absolute;
    width: 516px;
    height: 333px;
    background: var(--card);
    box-shadow: 0 6px 14px rgba(0,0,0,0.25);
    overflow: hidden;
  }
  .card--front { left: 182px; top: 157px; }
  .card--back { left: 173px; top: 697px; }

  /* Front */
  .brand-mark {
    position: absolute;
    left: 240px; top: 104px;
    width: 36px; height: 36px;
    background: var(--blue);
  }
  .brand-name {
    position: absolute;
    left: 0; right: 0; top: 165px;
    text-align: center;
    color: var(--grey);
    font-weight: 500;
    font-size: 22px;
    letter-spacing: 0.5px;
  }
  .brand-sub {
    position: absolute;
    left: 168px; width: 180px; top: 193px;
    display: flex; align-items: center; gap: 5px;
    color: var(--grey);
    font-weight: 500;
    font-size: 7.5px;
    letter-spacing: 2.4px;
    white-space: nowrap;
  }
  .brand-sub .rule { flex: 1; height: 1px; background: var(--grey-soft); }
  .tagline {
    position: absolute;
    left: 0; right: 0; top: 233px;
    text-align: center;
    color: var(--grey);
    font-size: 9px;
    line-height: 14.5px;
  }
  .tagline .since { font-size: 11.5px; display: block; margin-top: 1px; }

  /* Back */
  .person-name {
    position: absolute;
    left: 56px; top: 62px;
    color: var(--blue);
    font-weight: 500;
    font-size: 29px;
  }
  .person-title {
    position: absolute;
    left: 56px; top: 96px;
    color: var(--grey);
    font-size: 16px;
  }
  .contact {
    position: absolute;
    left: 56px; top: 146px;
    list-style: none;
    color: var(--grey);
    font-size: 15px;
    line-height: 20px;
  }
  .contact li { display: flex; align-items: center; gap: 9px; }
  .contact svg { width: 13px; height: 13px; fill: var(--grey-soft); }
  .back-name {
    position: absolute;
    left: 318px; width: 144px; top: 112px;
    text-align: center;
    color: var(--blue);
    font-weight: 500;
    font-size: 20px;
    letter-spacing: 0.5px;
    white-space: nowrap;
  }
  .flag {
    position: absolute;
    left: 30px; top: 272px;
    width: 51px; height: 36px;
    background: linear-gradient(135deg, var(--flag-blue) 0 35%, var(--flag-red) 35% 100%);
    opacity: 0.85;
  }
  .divider {
    position: absolute;
    left: 95px; top: 279px;
    width: 393px; height: 1px;
    background: var(--blue);
  }
  .services {
    position: absolute;
    left: 95px; top: 285px;
    width: 393px;
    display: flex; justify-content: space-between; align-items: center;
    color: var(--blue);
    font-size: 8px;
    letter-spacing: 0.2px;
    white-space: nowrap;
  }
  .services .dot { width: 2px; height: 2px; border-radius: 50%; background: var(--blue); }
</style>
</head>
<body>
  <section class="card card--front">
    <div class="brand-mark"></div>
    <div class="brand-name">MERIDIAN</div>
    <div class="brand-sub"><span class="rule"></span>FABRICATION INC<span class="rule"></span></div>
    <p class="tagline">PROUDLY SERVING THE COMMERCIAL<br>AND DEFENSE INDUSTRIES<span class="since">SINCE 1975</span></p>
  </section>

  <section class="card card--back">
    <h1 class="person-name">Dale Hartwin</h1>
    <p class="person-title">PRESIDENT</p>
    <ul class="contact">
      <li>
        <svg viewBox="0 0 16 16" aria-hidden="true"><path d="M1 3h14v10H1z M1 3l7 6 7-6" fill="none" stroke="#9a9a9a" stroke-width="1.6"/><path d="M2 4l6 5 6-5v8H2z"/></svg>
        Dale@meridianfab
      </li>
      <li>
        <svg viewBox="0 0 16 16" aria-hidden="true"><path d="M3.5 1l2.5 3-1.5 2c1 2 3 4 5 5l2-1.5 3 2.5-1.5 2.5C8 14.5 1.5 8 1 2.5z"/></svg>
        555-014-0192
      </li>
    </ul>
    <div class="back-name">MERIDIAN</div>
    <div class="flag" role="img" aria-label="Waving USA flag"></div>
    <div class="divider"></div>
    <div class="services">
      <span>WATERJET</span><span class="dot"></span>
      <span>COMPOSITE</span><span class="dot"></span>
      <span>PRECISION MACHINING</span><span class="dot"></span>
      <span>CLEAN ROOM MANUFACTURING</span>
    </div>
  </section>
</body>
</html>
```